Objective: Create a visually stunning and compelling PDF brochure that showcases The Orvelle Peak Lodge as the ultimate luxury hunting destination in Kyrgyzstan, specializing in Marco Polo and Ibex hunts. The PDF should evoke a sense of exclusivity, adventure, and the breathtaking beauty of the Tian Shan mountains, ultimately driving bookings.
Target Audience: High-net-worth individuals, discerning hunters seeking exceptional experiences, adventure travelers, and those interested in unique and luxurious wilderness experiences.
Overall Tone & Style: Sophisticated, elegant, and aspirational. Think high-end travel magazines combined with a touch of rugged adventure. Avoid anything that feels generic or overly commercial. The design should reflect the unparalleled nature of the lodge and the hunts offered. (I'm attaching a reference PDF that i like), as well as another instructions file. Drive link for photos: https://files.brankolu.net/share/folders/7KRM42PTbWq0vnzeHJ5sudYA913_c8LxE?mode=view
Another Link: https://files.brankolu.net/share/u/0/folders/5TWEpk-m8rzaqoLc2BnvXwiyeSKdfuGtm

```html
<!DOCTYPE html>
<html lang="en">
<head>
<meta charset="UTF-8">
<title>Dates &amp; Pricing — The Orvelle Peak Lodge</title>
<link href="https://fonts.googleapis.com/css2?family=Poppins:ital,wght@0,300;0,400;0,700;0,800;1,300&display=swap" rel="stylesheet">
<style>
  :root{
    --navy:#1f2c44;
    --ink:#27324a;
    --paper:#fbfbfa;
    --white:#ffffff;
    --photo-light:#cdbfae;
    --photo-mid:#8f7b66;
    --photo-dark:#4a4036;
  }
  *{margin:0;padding:0;box-sizing:border-box}
  html,body{width:1200px;height:675px;overflow:hidden}
  body{font-family:"Poppins",sans-serif;background:var(--paper);color:var(--ink);position:relative}
  .hero-photo{
    position:absolute;left:0;top:0;width:512px;height:675px;
    background:linear-gradient(160deg,var(--photo-light) 0%,#b6a48f 35%,var(--photo-mid) 65%,var(--photo-dark) 100%);
  }
  .hero-tag{
    position:absolute;left:31px;top:462px;transform-origin:0 0;transform:rotate(-90deg);
    color:var(--navy);font-size:12px;letter-spacing:10px;white-space:nowrap;font-weight:400;
  }
  .hero-title{
    position:absolute;left:30px;top:572px;color:var(--white);
    font-size:53px;font-weight:700;letter-spacing:-0.5px;white-space:nowrap;line-height:1;
  }
  .season-title{
    position:absolute;left:633px;top:78px;color:var(--navy);
    font-size:53px;font-weight:800;line-height:1;letter-spacing:-0.5px;
  }
  .season-dates{
    position:absolute;left:636px;top:136px;font-size:18.5px;font-weight:300;color:var(--ink);
  }
  .section-label{
    position:absolute;transform:translate(-50%,-50%) rotate(-90deg);
    color:var(--navy);font-size:18px;font-weight:700;letter-spacing:2.5px;white-space:nowrap;
  }
  .label-inclusions{left:610px;top:285px}
  .label-pricing{left:610px;top:494px}
  .incl-col{
    position:absolute;top:186px;width:253px;font-size:11.8px;line-height:18.3px;
    font-weight:300;text-align:justify;color:var(--ink);
  }
  .incl-col p{margin:0}
  .incl-col .gap{margin-top:18px}
  .col-a{left:636px}
  .col-b{left:919px;width:255px}
  .price-list{position:absolute;left:641px;top:438px;width:247px;font-weight:300;color:var(--ink)}
  .price-item{font-size:18.5px;line-height:21px;text-align:justify;margin-bottom:20px}
  .price-item b{font-weight:700;color:var(--navy)}
  .price-item i{font-size:15.5px;font-style:italic}
  .addons{
    position:absolute;left:895px;top:528px;width:305px;height:107px;
    background:var(--navy);border-radius:18px 0 0 18px;color:var(--white);
    padding:14px 20px 0 21px;font-size:18.5px;line-height:21px;
  }
  .addons b{font-weight:700}
  .addons .row{display:flex;justify-content:space-between}
</style>
</head>
<body>
  <div class="hero-photo" role="img" aria-label="Hunter in camouflage jacket and cap glassing the mountains through binoculars"></div>
  <div class="hero-tag">KYRGYZSTAN | 2025</div>
  <h1 class="hero-title">DATES &amp; PRICING</h1>

  <h2 class="season-title">SEASON DATES</h2>
  <p class="season-dates">August 15th, 2025 – November 30th, 2025</p>

  <div class="section-label label-inclusions">INCLUSIONS</div>
  <div class="incl-col col-a">
    <p>• Guide Hunt:</p>
    <p>7-day guided horseback hunt for Marco Polo Argali, Ibex or Both;</p>
    <p>Exclusive access to some of the finest hunting areas in Kyrgyzstan;</p>
    <p>Trophy skinning and field preparation.</p>
    <p class="gap">• Food &amp; Drink:</p>
    <p>Chef-prepared breakfast, packed lunch, and dinner;</p>
    <p>A selection of non-alcoholic beverages.</p>
  </div>
  <div class="incl-col col-b">
    <p>• Travel &amp; Logistics:</p>
    <p>Pre-arrival custom planning with the Summitrail Team;</p>
    <p>Round trip, fixed-time airport transfers to Bishkek.</p>
  </div>

  <div class="section-label label-pricing">PRICING</div>
  <div class="price-list">
    <p class="price-item">Marco Polo and Ibex COMBO <b>$39,500</b> <i>(min. 2 hunters)</i></p>
    <p class="price-item" style="text-align:left">Marco Polo Argali<br><b>$32,500</b> <i>(min. 2 hunters)</i></p>
    <p class="price-item" style="text-align:left">Mid-asian IBEX<br><b>$10,500</b> <i>(min. 2 hunters)</i></p>
  </div>

  <div class="addons">
    <b>POPULAR ADD-ONS</b>
    <div class="row"><span>WOLF</span><span>(Opportunistic):</span></div>
    <b>$2,500</b><br>
    <b>Extra Ibex: $5,500</b>
  </div>
</body>
</html>
```